Web page for analytics company

Now that I have a new logo, I need a webpage design that will use it to its potential. Am looking for a design that handles presentation and access to data well - like sites with blocks that provide direct access to content without going through a set of menus. More like an infographic. No left/right menu bar.

I want the logo (attached) against a black background, but not text - not a fan of trying to read white text on a dark screen.

The website - torvimbly.com - currently has four pages - home, who we are, by the numbers and a blog.

The site will be done in Squarespace.

My apologies for not responding promptly - big report due today.  I will be online tomorrow with answers and feedback. 

Thanks!

```html
<!DOCTYPE html>
<html lang="en">
<head>
<meta charset="utf-8">
<title>Torvimbly – Gender Equity Analytics</title>
<link href="https://fonts.googleapis.com/css2?family=Questrial&display=swap" rel="stylesheet">
<style>
:root{
  --black:#000;
  --orange:#f7941d;
  --ink:#111;
  --text:#444;
  --muted:#777;
  --line:#ddd;
  --panel:#ececec;
  --footer:#222;
  --footer-text:#aaa;
  --white:#fff;
}
*{box-sizing:border-box;margin:0;padding:0}
html,body{width:802px;height:1200px;overflow:hidden}
body{font-family:"Questrial",sans-serif;color:var(--text);background:var(--white)}
.site-header{height:53px;background:var(--black);position:relative}
.brand{position:absolute;left:135px;top:12px;display:flex;align-items:center;gap:6px;color:var(--white);font-size:21px}
.brand-dot{width:29px;height:29px;border-radius:50%;background:var(--orange)}
.menu-toggle{position:absolute;left:647px;top:19px;width:21px;height:18px}
.hero{position:relative;height:293px}
.hero-photo{position:absolute;inset:0;background:linear-gradient(100deg,#6f7f86 0%,#a9b6bc 30%,#cdd7dc 55%,#b8c6cc 80%,#9fb0b7 100%)}
.hero-card{position:absolute;left:360px;top:126px;width:308px;height:87px;background:rgba(240,243,245,.9);border-radius:2px;text-align:center;padding-top:10px}
.hero-card h1{font-weight:400;font-size:19px;color:var(--ink);letter-spacing:-.3px}
.hero-card .tagline{font-size:11.5px;color:#333;margin:0 15px;padding-bottom:3px;border-bottom:1px solid #999}
.hero-card .lead{font-size:8.5px;color:#555;line-height:12px;margin-top:7px}
.testimonials{height:216px;text-align:center;padding-top:40px}
h2{font-weight:400;font-size:25px;color:var(--ink);letter-spacing:-.5px}
.quote{position:relative;width:472px;margin:10px auto 0;border:1px solid var(--line);padding:11px 20px;font-size:9.5px;line-height:15.5px;color:#555}
.quote::after{content:"";position:absolute;left:50%;bottom:-6px;width:10px;height:10px;background:var(--white);border-right:1px solid var(--line);border-bottom:1px solid var(--line);transform:translateX(-50%) rotate(45deg)}
.quote-source{font-size:8.5px;color:#333;margin-top:12px}
.btn{display:inline-block;background:var(--orange);color:var(--white);font-family:inherit;font-size:9.5px;border:0;border-radius:2px}
.btn-more{width:75px;height:20px;line-height:20px;margin-top:10px}
.about{height:240px;background:var(--panel);text-align:center;padding-top:25px}
.about p{width:540px;margin:4px auto 0;font-size:8.3px;line-height:13.6px;color:#444}
.about strong{color:var(--ink)}
.subscribe{height:250px;text-align:center;padding-top:38px}
.subscribe form{width:404px;margin:12px auto 0}
.field{display:block;width:100%;height:23px;border:1px solid var(--line);margin-bottom:9px;padding-left:15px;font-family:inherit;font-size:7.5px;color:var(--muted);text-align:left;line-height:21px}
.btn-subscribe{width:101px;height:19px;line-height:19px;margin-top:5px}
.site-footer{height:116px;background:var(--footer);position:relative}
.feed{position:absolute;top:22px;width:170px;font-size:7px;line-height:11.7px;color:var(--footer-text)}
.feed h3{font-weight:400;font-size:10px;color:var(--white);margin-bottom:2px}
.feed time{display:block;color:var(--white)}
.follow{position:absolute;left:134px;top:92px;background:#e8eef2;border:1px solid #bbb;font-size:6px;color:#246;padding:1px 4px}
.copyright{height:32px;background:var(--footer);border-top:1px solid #3a3a3a;font-size:8.5px;color:#ccc;padding:11px 0 0 135px}
</style>
</head>
<body>
<header class="site-header">
  <div class="brand"><span class="brand-dot"></span>Torvimbly</div>
  <svg class="menu-toggle" viewBox="0 0 21 18" aria-label="Menu">
    <rect y="0" width="21" height="3" fill="#fff"/><rect y="5" width="21" height="3" fill="#fff"/>
    <rect y="10" width="21" height="3" fill="#fff"/><rect y="15" width="21" height="3" fill="#fff"/>
  </svg>
</header>

<section class="hero">
  <div class="hero-photo" role="img" aria-label="Photo of a man in a striped shirt working on a laptop in a bright office"></div>
  <div class="hero-card">
    <h1>GENDER EQUITY ANALYTICS</h1>
    <p class="tagline">Enhancing Performance Through A Gender Lens</p>
    <p class="lead">"we Keep Statistics On Everything We Care About, From Rbis To Roi,<br>The Daily Ups And Downs Of The Dow And Our Bank Accounts...</p>
  </div>
</section>

<section class="testimonials">
  <h2>What People Says</h2>
  <blockquote class="quote">So If We're Serious About Narrowing The Gender Gap And Helping More Girls And Women,<br>Then We Must Get Serious About Gathering And Analyzing The Data That Tell The Tale."</blockquote>
  <p class="quote-source">- Former Secretary of State Eleanor Whitcombe, July 2012-</p>
  <span class="btn btn-more">View More</span>
</section>

<section class="about">
  <h2>About us</h2>
  <p>As much as we'd like to think that treating everyone equally is the best strategy for fairness, the reality is that the differences in the lives of women and men have to be taken into account to ensure that organizations, programs, services, and yes, even public policy treat women and men in ways that achieve gender equity.<br>
  That's where Torvimbly - Gender Equity Analytics - comes in. Using the data-driven tools of gender analysis, we can help you determine if gender equity is being achieved - in businesses and organizations, in the planning and implementation of programs and services, and in the development and enforcement of public policy.<br>
  The evidence is in: analysis of organizational performance metrics that date back to the 1980s shows there is a clear relationship between better results and diverse leadership. Senior executives who ignore the data do so to their detriment. They're literally leaving money on the table.<br>
  But numbers don't tell the whole story. Organizations have to be willing to dig deep to discover where the biases are buried - in the organization's culture, in governance practices, in talent management strategies, and in personal values and belief systems.<br>
  Find out what a gender equity audit can do for your organization. Contact us at <strong>jmarlow@torvimbly.com or 555-203-0148.</strong></p>
</section>

<section class="subscribe">
  <h2>Subscribe To Our Mailing List</h2>
  <form>
    <span class="field">Email Address</span>
    <span class="field">First Name</span>
    <span class="field">Last Name</span>
    <span class="btn btn-subscribe">Suscribe Now</span>
  </form>
</section>

<footer>
  <div class="site-footer">
    <article class="feed" style="left:137px">
      <h3>Council on Parity</h3>
      Swedish video closes the gender pay gap in 47 seconds: we just need to "be a man!" Pagebook app let's you try it. http://lnk.to/QpR7sVn2
      <time>about a day ago</time>
    </article>
    <article class="feed" style="left:317px">
      <h3>Council on Parity</h3>
      Marlowe describes life-stage approach Ventrix Ltd. takes to women's career advancement. #equalitymeansjobs More info: http://lnk.to/Hx4mWd9k
      <time>about 5 days ago</time>
    </article>
    <article class="feed" style="left:497px">
      <h3>Council on Parity</h3>
      Need to stop using "choices" as an excuse for gender inequality. Keystone says even w/ same choices women do less well. #equalitymeansjobs
      <time>about 5 days ago</time>
    </article>
    <span class="follow">Follow @Council_Parity</span>
  </div>
  <div class="copyright">Copyright © 2014 Torvimbly. All rights reserved.</div>
</footer>
</body>
</html>
```